IT services company needs a business card designed

-2 sided business card.-Front is going to be the logo raised (3D floating effect) on a black background. Make the logos spider web shiny silver and keep the spider the same design. -Back needs to have the following information:Darrel Sotho, Managing Partner, Cell: 738-402-1954, Website: Plankhorn.com, Email: Darrel@Plankhorn.com
Target Market(s)
IT Services
Industry/Entity Type
It Company
Contact Information for Business Card
-2 sided business card.
-Front is going to be the logo raised (3D floating effect) on a black background. Make the logos spider web shiny silver and keep the spider the same design.
-Back needs to have the following information:
Darrel Sotho, Managing Partner, Cell: 738-402-1954, Website: Plankhorn.com, Email: Darrel@Plankhorn.com

```html
<!DOCTYPE html>
<html lang="en">
<head>
<meta charset="utf-8">
<title>Plankhorn Business Card</title>
<link href="https://fonts.googleapis.com/css2?family=Overpass:wght@400;500;600&display=swap" rel="stylesheet">
<style>
  :root {
    --page-bg: #dcdcdc;
    --card-bg: #eef0f5;
    --ink: #111318;
    --blue: #3a6fd8;
    --blue-light: #5aa0e3;
    --web-tone: #9fb9de;
    --web-faint: #cfdcef;
  }
  * { margin: 0; padding: 0; box-sizing: border-box; }
  html, body { width: 1200px; height: 1200px; overflow: hidden; }
  body {
    background: var(--page-bg);
    font-family: "Overpass", sans-serif;
    color: var(--ink);
    display: flex;
    flex-direction: column;
    align-items: center;
    justify-content: center;
    gap: 60px;
  }
  .card {
    position: relative;
    width: 900px;
    height: 514px;
    background: var(--card-bg);
    box-shadow: 0 14px 40px rgba(0,0,0,0.18);
    overflow: hidden;
  }
  .card svg.layer { position: absolute; inset: 0; }
  .web-art {
    position: absolute;
    background: radial-gradient(circle, var(--web-tone) 0%, rgba(159,185,222,0.35) 55%, rgba(159,185,222,0) 75%);
  }
  .web-corner {
    position: absolute;
    background: radial-gradient(circle at 30% 50%, rgba(120,130,150,0.35) 0%, rgba(120,130,150,0) 70%);
  }
  .web-corner.right {
    background: radial-gradient(circle at 70% 60%, rgba(90,160,227,0.4) 0%, rgba(90,160,227,0) 70%);
  }
  .wordmark {
    position: absolute;
    font-weight: 500;
    letter-spacing: 2px;
    color: var(--ink);
    text-align: center;
  }
  /* front */
  .front .web-art { left: 380px; top: 110px; width: 160px; height: 150px; }
  .front .wordmark { left: 0; right: 0; top: 270px; font-size: 42px; }
  .front .web-corner.left { left: 0; top: 40px; width: 220px; height: 170px; }
  .front .web-corner.right { right: 0; top: 250px; width: 190px; height: 220px; }
  /* back */
  .back .web-art { left: 95px; top: 70px; width: 120px; height: 110px; }
  .back .wordmark { left: 50px; width: 220px; top: 188px; font-size: 28px; }
  .back .spider-decor {
    position: absolute; left: 500px; top: 300px; width: 400px; height: 214px;
    background: radial-gradient(ellipse at 70% 70%, var(--web-faint) 0%, rgba(207,220,239,0.5) 45%, rgba(207,220,239,0) 75%);
  }
  .person {
    position: absolute; right: 40px; top: 100px; text-align: right;
  }
  .person-name { font-size: 56px; font-weight: 500; line-height: 1; }
  .person-title { font-size: 28px; font-weight: 400; margin-top: 2px; }
  .contact {
    position: absolute; left: 300px; font-size: 22px; font-weight: 500;
  }
  .contact.phone { top: 248px; }
  .contact.email { top: 308px; }
  .contact.web { top: 378px; }
</style>
</head>
<body>
  <section class="card front" aria-label="Card front">
    <div class="web-corner left" role="img" aria-label="Corner spider web decoration"></div>
    <div class="web-corner right" role="img" aria-label="Corner spider web decoration"></div>
    <div class="web-art" role="img" aria-label="Spider web emblem area"></div>
    <div class="wordmark">PLANKHORN</div>
  </section>

  <section class="card back" aria-label="Card back">
    <svg class="layer" width="900" height="514" viewBox="0 0 900 514">
      <defs>
        <linearGradient id="bandGrad" x1="0" x2="1">
          <stop offset="0" stop-color="#3a6fd8"/>
          <stop offset="1" stop-color="#5aa0e3"/>
        </linearGradient>
      </defs>
      <polygon class="top-band" points="0,0 900,0 900,50 540,50 508,16 0,16" fill="url(#bandGrad)"/>
      <g class="connector" stroke="#3a6fd8" stroke-width="6" fill="none">
        <polyline points="30,300 75,262 250,262"/>
        <line x1="40" y1="322" x2="250" y2="322"/>
        <polyline points="30,345 75,392 250,392"/>
      </g>
      <circle cx="0" cy="322" r="48" fill="#3a6fd8"/>
      <g fill="#3a6fd8">
        <circle cx="270" cy="262" r="22"/>
        <circle cx="270" cy="322" r="22"/>
        <circle cx="270" cy="392" r="22"/>
      </g>
      <path class="icon-phone" d="M262 252 q-3 3 0 10 q4 9 12 13 q6 2 8 -1 l-5 -5 q-2 2 -4 1 q-5 -3 -7 -8 q0 -2 2 -3 z" fill="#fff"/>
      <g class="icon-mail" stroke="#fff" stroke-width="2" fill="none">
        <rect x="259" y="314" width="22" height="16"/>
        <polyline points="259,314 270,324 281,314"/>
      </g>
      <g class="icon-globe" stroke="#fff" stroke-width="1.8" fill="none">
        <circle cx="270" cy="392" r="11"/>
        <ellipse cx="270" cy="392" rx="5" ry="11"/>
        <line x1="259" y1="392" x2="281" y2="392"/>
        <line x1="261" y1="386" x2="279" y2="386"/>
        <line x1="261" y1="398" x2="279" y2="398"/>
      </g>
    </svg>
    <div class="spider-decor" role="img" aria-label="Faint spider web decoration"></div>
    <div class="web-art" role="img" aria-label="Spider web emblem area"></div>
    <div class="wordmark">PLANKHORN</div>
    <div class="person">
      <div class="person-name">Darrel Sotho</div>
      <div class="person-title">Managing Partner</div>
    </div>
    <div class="contact phone">738-402-1954</div>
    <div class="contact email">Darrel@Plankhorn.com</div>
    <div class="contact web">www.Plankhorn.com</div>
  </section>
</body>
</html>
```